" Empresa jovem, em franca expansao, com necessidade de ampliar e qualificar sua carteira de clientes, buscando aprimorar sua identidade visual para se destacar em uma concorrência com pouco investimento nesse fundamento corporativo e potencializar sua apresentaçao a clientes de grande porte. "

```html
<!DOCTYPE html>
<html lang="pt-BR">
<head>
<meta charset="utf-8">
<title>Afiadora Serrana — Cartão de visita</title>
<link href="https://fonts.googleapis.com/css2?family=Ubuntu:wght@400;500;700&display=swap" rel="stylesheet">
<style>
  :root {
    --navy: #13355c;
    --green: #1fa04a;
    --white: #ffffff;
    --backdrop: #e9ebee;
    --ink-soft: #d7e1ee;
  }
  * { margin: 0; padding: 0; box-sizing: border-box; }
  html, body { width: 1200px; height: 1200px; overflow: hidden; }
  body {
    background: var(--backdrop);
    font-family: "Ubuntu", sans-serif;
    display: flex;
    flex-direction: column;
    align-items: center;
    justify-content: center;
    gap: 60px;
  }
  .card {
    width: 900px;
    height: 500px;
    border-radius: 22px;
    position: relative;
    overflow: hidden;
    box-shadow: 0 6px 20px rgba(0,0,0,0.12);
  }
  .card-front {
    background: var(--white);
    display: flex;
    align-items: center;
    justify-content: center;
  }
  .brand {
    display: flex;
    align-items: center;
    gap: 22px;
    color: var(--navy);
    font-weight: 700;
  }
  .brand-square { background: var(--navy); flex: none; }
  .card-front .brand { font-size: 64px; letter-spacing: 1px; }
  .card-front .brand-square { width: 90px; height: 90px; }

  .card-back { background: var(--navy); color: var(--white); }
  .accent-stripe {
    position: absolute;
    left: 58px; top: 0;
    width: 52px; height: 100%;
    background: var(--green);
  }
  .accent-line {
    position: absolute;
    left: 120px; top: 0;
    width: 6px; height: 100%;
    background: var(--white);
  }
  .contact-icons {
    position: absolute;
    left: 58px; top: 190px;
    width: 52px;
    display: flex;
    flex-direction: column;
    align-items: center;
    gap: 22px;
  }
  .contact-icons svg { width: 26px; height: 26px; display: block; }
  .person {
    position: absolute;
    left: 170px; top: 70px;
  }
  .person-name { font-size: 40px; font-weight: 500; }
  .person-role { font-size: 22px; margin-top: 4px; color: var(--ink-soft); }
  .contact-list {
    position: absolute;
    left: 170px; top: 190px;
    list-style: none;
    font-size: 29px;
    line-height: 40px;
  }
  .card-back .brand {
    position: absolute;
    right: 48px; bottom: 60px;
    color: var(--white);
    font-size: 30px;
    gap: 12px;
  }
  .card-back .brand-square { width: 40px; height: 40px; background: var(--white); }
</style>
</head>
<body>
  <section class="card card-front">
    <div class="brand">
      <span class="brand-square"></span>
      <span class="brand-name">AFIADORA SERRANA</span>
    </div>
  </section>

  <section class="card card-back">
    <div class="accent-stripe"></div>
    <div class="accent-line"></div>

    <div class="contact-icons">
      <svg viewBox="0 0 24 24" aria-label="endereço"><rect x="3" y="6" width="18" height="12" fill="none" stroke="#fff" stroke-width="2"/><path d="M3 6l9 7 9-7" fill="none" stroke="#fff" stroke-width="2"/></svg>
      <svg viewBox="0 0 24 24" aria-label="telefone"><path d="M6 3l4 4-2 3c1 2 4 5 6 6l3-2 4 4-3 3C10 21 3 14 3 6z" fill="#fff"/></svg>
      <svg viewBox="0 0 24 24" aria-label="e-mail"><circle cx="12" cy="12" r="4" fill="none" stroke="#fff" stroke-width="2"/><path d="M16 8v6c0 2 4 2 4-2a8 8 0 1 0-4 7" fill="none" stroke="#fff" stroke-width="2"/></svg>
      <svg viewBox="0 0 24 24" aria-label="site"><path d="M12 2a7 7 0 0 0-7 7c0 5 7 13 7 13s7-8 7-13a7 7 0 0 0-7-7z" fill="#fff"/><circle cx="12" cy="9" r="2.5" fill="#1fa04a"/></svg>
    </div>

    <div class="person">
      <p class="person-name">Paulo Henrique</p>
      <p class="person-role">Diretor</p>
    </div>

    <ul class="contact-list">
      <li>Rua das Acácias, 215 Centro</li>
      <li>Serra Alta&nbsp; MG</li>
      <li>31 4000-1234/31 9000-5678</li>
      <li>paulo@serrana.com.br</li>
      <li>www.serrana.com.br</li>
    </ul>

    <div class="brand">
      <span class="brand-square"></span>
      <span class="brand-name">AFIADORA SERRANA</span>
    </div>
  </section>
</body>
</html>
```